Graphic that shows our management philosophy and strategy

We need a graphic design that shows our management framework. Attached is my (poor) attempt at making this look good. Please refer to this file:

Please note that the other 3 files in the attachments are just examples of works that I think are visually appealing.

Up to five colors can be used but less is fine also. If colors are used, then please use ones that are close to the colors in the graphic. This graphic will be used to show employees how and why we are doing what we do.

If you could create the graphic in Powerpoint, that would be ideal, but am willing to take any graphic format if it looks great

Target Market(s)

Internal employees

Industry/Entity Type

Graphic Design

Requirements
Must have
• Must show a hierarchy vertically between the various levels
Nice to have
• Using a pyramid as the background structure might be nice
• The last 3 attachments are examples I found that I found visually attractive.

```html
<!DOCTYPE html>
<html lang="en">
<head>
<meta charset="utf-8">
<title>Management Framework – Aspirations and Values</title>
<link rel="stylesheet" href="https://fonts.googleapis.com/css2?family=Arimo:ital,wght@0,400;0,700;1,700&family=Archivo+Narrow:ital@1&display=swap">
<style>
  :root {
    --canvas: #ffffff;
    --backdrop-light: #eef0f3;
    --backdrop-dark: #d9dde3;
    --heading: #1d3a5c;
    --side-label: #8b9099;
    --sheet-top: #7fd6dc;
    --sheet-mid: #4bbcc6;
    --sheet-bottom: #2c9aa8;
    --sheet-text: #10303a;
    --tab: #ffffff;
    --shadow: rgba(40, 55, 70, 0.28);
  }
  html, body {
    margin: 0;
    padding: 0;
    width: 779px;
    height: 1200px;
    overflow: hidden;
    background: var(--canvas);
  }
  .framework {
    position: relative;
    width: 779px;
    height: 1200px;
  }
  .tier {
    position: absolute;
    left: 0;
    width: 779px;
    background: linear-gradient(160deg, var(--backdrop-light), var(--backdrop-dark));
  }
  .tier--aspirations { top: 0; height: 535px; }
  .tier--values { top: 636px; height: 564px; }
  .tier-title {
    position: absolute;
    margin: 0;
    font-family: "Arimo", sans-serif;
    font-style: italic;
    font-weight: 700;
    font-size: 27px;
    letter-spacing: 0.5px;
    color: var(--heading);
  }
  .tier--aspirations .tier-title { left: 26px; top: 18px; }
  .tier--values .tier-title { left: 31px; top: 92px; }
  .tier-question {
    position: absolute;
    left: 124px;
    margin: 0;
    font-family: "Archivo Narrow", sans-serif;
    font-style: italic;
    font-size: 36px;
    line-height: 45px;
    letter-spacing: 2px;
    color: var(--side-label);
  }
  .tier--aspirations .tier-question { top: 190px; }
  .tier--values .tier-question { top: 252px; }
  .sheet {
    position: absolute;
    left: 0;
    top: 0;
    width: 779px;
    height: 100%;
  }
  .sheet-text {
    font-family: "Arimo", sans-serif;
    font-size: 21px;
    fill: var(--sheet-text);
  }
  .sheet-text--strong { font-weight: 700; }
  .sheet-tab { fill: var(--tab); }
</style>
</head>
<body>
<main class="framework">

  <section class="tier tier--aspirations">
    <h2 class="tier-title">ASPIRATIONS</h2>
    <p class="tier-question">WHY<br>WE<br>ARE<br>HERE</p>
    <svg class="sheet" viewBox="0 0 779 535">
      <defs>
        <linearGradient id="sheetFillTop" x1="0" y1="0" x2="0.3" y2="1">
          <stop offset="0" stop-color="var(--sheet-top)"/>
          <stop offset="0.55" stop-color="var(--sheet-mid)"/>
          <stop offset="1" stop-color="var(--sheet-bottom)"/>
        </linearGradient>
        <filter id="sheetShadowTop" x="-10%" y="-10%" width="130%" height="130%">
          <feDropShadow dx="8" dy="12" stdDeviation="9" flood-color="var(--shadow)"/>
        </filter>
      </defs>
      <path d="M247,80 Q470,40 706,14 Q702,240 690,468 Q450,462 228,530 Q240,300 247,80 Z"
            fill="url(#sheetFillTop)" filter="url(#sheetShadowTop)"/>
      <g class="sheet-tabs">
        <rect class="sheet-tab" x="280" y="70" width="50" height="18" rx="4" transform="rotate(-6 305 79)"/>
        <rect class="sheet-tab" x="390" y="58" width="50" height="18" rx="4" transform="rotate(-6 415 67)"/>
        <rect class="sheet-tab" x="500" y="46" width="50" height="18" rx="4" transform="rotate(-6 525 55)"/>
        <rect class="sheet-tab" x="610" y="34" width="50" height="18" rx="4" transform="rotate(-6 635 43)"/>
      </g>
      <g class="aspiration-list" transform="rotate(-6 470 360)" text-anchor="end">
        <text class="sheet-text" x="652" y="178">Purpose</text>
        <text class="sheet-text" x="646" y="204">Make Solar Stronger</text>
        <text class="sheet-text" x="640" y="246">Vision</text>
        <text class="sheet-text" x="652" y="272">A world with solar on every rooftop</text>
        <text class="sheet-text" x="640" y="308">Purpose</text>
        <text class="sheet-text sheet-text--strong" x="656" y="334">Help installers become solar heroes</text>
        <text class="sheet-text" x="640" y="374">Goal</text>
        <text class="sheet-text" x="650" y="408">Lead every market we participate in</text>
      </g>
    </svg>
  </section>

  <section class="tier tier--values">
    <svg class="sheet" viewBox="0 0 779 564">
      <defs>
        <linearGradient id="sheetFillBottom" x1="0" y1="0" x2="0.3" y2="1">
          <stop offset="0" stop-color="var(--sheet-top)"/>
          <stop offset="0.55" stop-color="var(--sheet-mid)"/>
          <stop offset="1" stop-color="var(--sheet-bottom)"/>
        </linearGradient>
        <filter id="sheetShadowBottom" x="-10%" y="-10%" width="130%" height="130%">
          <feDropShadow dx="8" dy="12" stdDeviation="9" flood-color="var(--shadow)"/>
        </filter>
      </defs>
      <path d="M247,56 Q470,36 706,44 Q702,220 690,392 Q450,400 228,470 Q240,260 247,56 Z"
            fill="url(#sheetFillBottom)" filter="url(#sheetShadowBottom)"/>
      <g class="sheet-tabs">
        <rect class="sheet-tab" x="280" y="88" width="50" height="18" rx="4" transform="rotate(-2 305 97)"/>
        <rect class="sheet-tab" x="390" y="84" width="50" height="18" rx="4" transform="rotate(-2 415 93)"/>
        <rect class="sheet-tab" x="500" y="82" width="50" height="18" rx="4" transform="rotate(-1 525 91)"/>
        <rect class="sheet-tab" x="610" y="82" width="50" height="18" rx="4"/>
      </g>
      <g class="value-list">
        <text class="sheet-text" x="260" y="228">Be One<tspan x="260" dy="24">Team</tspan></text>
        <text class="sheet-text" x="364" y="260">Do the Right<tspan x="364" dy="24">Thing</tspan></text>
        <text class="sheet-text" x="447" y="324">Embrace<tspan x="447" dy="24">Charge</tspan></text>
        <text class="sheet-text" x="546" y="366">Produce More<tspan x="546" dy="24">With Less</tspan></text>
      </g>
    </svg>
    <h2 class="tier-title">VALUES</h2>
    <p class="tier-question">HOW<br>WE<br>ACT</p>
  </section>

</main>
</body>
</html>
```